Website Landing Page for Brightfall Systems

Create a custom designed website landing page for our business. Looking for a professional upscale design that incorporates our logo and logo colors into the theme. I want a standard fixed frame website, not a constant scrolling format that seems to be the trend. To start with I'm looking for more of the graphic design part, maybe a concept or theme, I don't expect to see a finished project. Not interested in generic templates or layouts.

The name of our company is Brightfall Systems and I've attached our logo below. I'd like to have the web page have the same look and feel of our logo, as well as the colors. Our company, Brightfall Systems does system design, installation, and programming, of residential and commercial Audio/Video and Automation systems. We do home theaters, lighting and building automation, video conferencing systems, security camera installations, conference rooms, projectors, distributed audio systems, and similar Technology projects. This will be a professional services/informational website. We will not sell products on this website. This website will be used to advertise our company and communicate our services to prospective customers. Having a well designed, professional and clean website is one way we want to distinguish our company from the competition.

Here are some examples of what I consider a professional well designed website
http://www.qorlamstudio.com/Work/

Last year we had our tradlo store designed (with PixelMarket) and I'm really happy with the way it turned out. You can see it at www.HolvenGearDepot.com I consider this to be a great design and looking for the same level of quality with this new website. However, do not copy or use any part of this design in this new project. This tradlo store is completely separate from our other company Brightfall Systems. I only mention this tradlo store an an example of good work.

Reason: Still going through designs.

Reason: Still working on project and have not had time to review all designs and request revisions.

Reason: Sill going through designs and requesting revisions

Reason: still going through all the submissions we received.

Target Market(s)

People interested in Audio/Video, home theaters, home automation. We do sales, system design, and programming. We typically work on larger projects with both residential and commercial customers.

Industry/Entity Type

Business

Number of Pages Required

1 page

Requirements
Must have
• Great design elements. Please use a white background. I think white goes well with our logo colors.

```html
<!DOCTYPE html>
<html lang="en">
<head>
<meta charset="utf-8">
<title>Brightfall Systems</title>
<link href="https://fonts.googleapis.com/css2?family=Fira+Sans:wght@500;700&family=Roboto:wght@300;400;500&family=Roboto+Slab:wght@400;700&family=Raleway:wght@400;500&display=swap" rel="stylesheet">
<style>
:root{
  --blue:#1b8fe0;
  --navy:#0e5fb3;
  --sky:#18b4e8;
  --green:#6abd45;
  --green-dark:#5aa832;
  --ink:#333;
  --muted:#7a7a7a;
  --footer:#1a6e9e;
  --white:#fff;
}
*{box-sizing:border-box;margin:0;padding:0}
html,body{width:842px;height:1200px;overflow:hidden;background:var(--white)}
body{position:relative;font-family:"Roboto",sans-serif;color:var(--ink)}
.abs{position:absolute}
.hero{left:0;top:0;width:842px;height:374px;background:linear-gradient(160deg,#e9dcc3 0%,#c7b69a 35%,#8a7a63 65%,#5c4e3e 100%)}
.header{left:114px;top:0;width:614px;height:70px;background:var(--white)}
.brand{left:18px;top:20px;display:flex;align-items:center;gap:8px}
.brand-dot{width:28px;height:28px;border-radius:50%;border:4px solid var(--blue)}
.brand-name{font-family:"Fira Sans",sans-serif;font-weight:500;font-size:15px;color:var(--blue);line-height:1.05;text-transform:uppercase}
.contact{right:16px;top:16px;text-align:left}
.contact-label{font-family:"Roboto Slab",serif;font-size:11px;font-weight:700;color:var(--ink);display:flex;align-items:center;gap:4px}
.contact-phone{font-family:"Roboto Slab",serif;font-weight:700;font-size:16px;color:var(--green);margin-left:20px}
.nav{left:114px;top:70px;width:614px;height:27px;background:var(--blue);border-radius:0 0 4px 4px;display:flex;align-items:center}
.nav a{font-family:"Roboto Slab",serif;color:var(--white);font-size:11px;text-decoration:none;height:27px;line-height:27px;text-align:center;border-right:1px solid rgba(0,0,0,.12)}
.nav .social{margin-left:auto;display:flex;gap:12px;padding-right:14px}
.nav .social span{width:9px;height:9px;border-radius:50%;background:var(--white)}
.hero-title{left:267px;top:202px;width:309px;height:44px;background:rgba(40,40,40,.8);color:var(--white);font-family:"Fira Sans",sans-serif;font-weight:700;font-size:36px;text-align:center;line-height:46px;letter-spacing:-.5px}
.hero-sub{left:219px;top:248px;width:402px;height:34px;background:rgba(90,168,50,.9);color:var(--white);font-family:"Fira Sans",sans-serif;font-weight:700;font-size:20px;text-align:center;line-height:34px;letter-spacing:-.5px}
.side-tabs{left:810px;top:198px;width:32px}
.side-tab{height:31px;display:flex;flex-direction:column;align-items:center;justify-content:center;color:var(--white);font-size:5px;font-weight:500;gap:2px}
.side-tab.call{background:#4a7fd6;border-radius:4px 0 0 0}
.side-tab.email{background:#1ca7a8;border-radius:0 0 0 4px}
.services{left:0;top:374px;width:842px;height:179px;display:flex}
.service{height:179px;color:var(--white);text-align:center;padding-top:37px}
.service h2{font-family:"Roboto Slab",serif;font-weight:700;font-size:23px;margin-top:6px}
.service p{font-size:7px;line-height:9.6px;margin:10px auto 0;width:226px}
.svc-design{width:278px;background:var(--sky)}
.svc-install{width:282px;background:var(--navy)}
.svc-program{width:282px;background:var(--green)}
.about-photo{left:0;top:553px;width:499px;height:264px;background:linear-gradient(90deg,#f2f2f2 0%,#8a6048 25%,#6e4a36 60%,#e9e9e9 90%)}
.about-text{left:499px;top:553px;width:343px;height:264px;background:#f4f4f4;padding:50px 0 0 13px}
.about-text .kicker{font-size:13px;font-weight:300;color:var(--ink)}
.about-text h3{font-family:"Fira Sans",sans-serif;font-weight:500;font-size:23px;color:#1a6e9e;margin-top:1px}
.about-text .lead{font-style:italic;font-size:8.5px;line-height:13px;color:var(--ink);width:220px;margin-top:6px}
.about-text .body{font-size:7.5px;line-height:11px;color:var(--muted);width:216px;margin-top:8px}
.deals-title{left:0;top:838px;width:842px;text-align:center;font-family:"Fira Sans",sans-serif;font-weight:500;font-size:23px;color:var(--green)}
.deals-intro{left:140px;top:878px;width:562px;text-align:center;font-size:7px;line-height:11px;color:var(--muted)}
.deals-rule{left:0;top:914px;width:842px;height:6px;background:#e6f1f7}
.deals{left:0;top:920px;width:842px;height:161px;display:flex}
.deal{position:relative;height:161px}
.deal-label{position:absolute;left:0;bottom:0;width:100%;height:32px;background:rgba(33,96,160,.85);color:var(--white);font-size:7px;font-weight:500;text-align:center;line-height:32px;text-transform:uppercase}
.cta{left:0;top:1101px;width:842px;text-align:center;font-family:"Raleway",sans-serif;font-size:13px;color:var(--ink)}
.cta a{color:var(--green);font-weight:500}
.footer{left:0;top:1133px;width:842px;height:67px;background:var(--footer);text-align:center;color:var(--white)}
.footer .social{display:flex;justify-content:center;gap:7px;margin-top:26px}
.footer .social span{width:16px;height:16px;border-radius:50%;border:1px solid var(--white)}
.footer p{font-size:11px;margin-top:8px;letter-spacing:.3px}
</style>
</head>
<body>
<div class="abs hero" role="img" aria-label="Photo of a bright living room with a large wall-mounted screen, sofa and speakers"></div>

<header class="abs header">
  <div class="abs brand"><span class="brand-dot"></span><span class="brand-name">Brightfall<br>Systems</span></div>
  <div class="abs contact">
    <div class="contact-label"><svg width="14" height="14" viewBox="0 0 14 14"><circle cx="7" cy="7" r="6" fill="none" stroke="#1b8fe0" stroke-width="1.2"/><path d="M4.5 4.3c.4-.4.8-.4 1 0l.6 1c.2.3 0 .6-.2.8l-.3.3c.4.8 1 1.4 1.8 1.8l.3-.3c.2-.2.5-.4.8-.2l1 .6c.4.2.4.6 0 1-.8.8-1.8.6-3-.3-1.2-.9-2-2-2.3-3-.2-.6-.1-1.2.3-1.7z" fill="#1b8fe0"/></svg>CONTACT WITH US</div>
    <div class="contact-phone">800-555-0192</div>
  </div>
</header>
<nav class="abs nav">
  <a href="#" style="width:70px">Home</a>
  <a href="#" style="width:107px">About Us</a>
  <a href="#" style="width:98px">Products</a>
  <a href="#" style="width:95px">Services</a>
  <a href="#" style="width:96px;border-right:none">Contact Us</a>
  <div class="social"><span></span><span></span><span></span><span></span></div>
</nav>

<div class="abs hero-title">YOUR SHOP</div>
<div class="abs hero-sub">IT'S UNIQUE, IT'S COMPLETE.</div>

<div class="abs side-tabs">
  <div class="side-tab call"><svg width="12" height="12" viewBox="0 0 12 12"><path d="M2.5 1.5c.4-.4.9-.4 1.1 0l.8 1.3c.2.4 0 .7-.2.9l-.4.4c.5 1 1.3 1.8 2.3 2.3l.4-.4c.2-.2.6-.4.9-.2l1.3.8c.4.2.4.7 0 1.1-1 1-2.3.8-3.8-.4S2.5 4.6 2.3 3.6c-.1-.8 0-1.5.2-2.1z" fill="none" stroke="#fff" stroke-width=".9"/></svg>CALL</div>
  <div class="side-tab email"><svg width="14" height="10" viewBox="0 0 14 10"><rect x=".5" y=".5" width="13" height="9" fill="none" stroke="#fff"/><path d="M.5.5 7 6l6.5-5.5" fill="none" stroke="#fff"/></svg>EMAIL</div>
</div>

<section class="abs services">
  <div class="service svc-design">
    <svg width="32" height="30" viewBox="0 0 32 30"><rect x="1" y="1" width="12" height="8" fill="none" stroke="#fff" stroke-width="2"/><rect x="19" y="21" width="12" height="8" fill="none" stroke="#fff" stroke-width="2"/><path d="M16 5h14M4 15h24M26 11l4 4-4 4M6 25h10M8 21l-4 4 4 4" fill="none" stroke="#fff" stroke-width="2"/></svg>
    <h2>SYSTEM DESIGN</h2>
    <p>Lorem Ipsum is simply dummy text of the printing and typesetting industry. Lorem Ipsum has been the industry's standard dummy text ever since the 1500s, when an unknown printer took...</p>
  </div>
  <div class="service svc-install">
    <svg width="30" height="30" viewBox="0 0 30 30"><circle cx="14" cy="13" r="8" fill="none" stroke="#fff" stroke-width="5" stroke-dasharray="4 2.3"/><circle cx="14" cy="13" r="4" fill="none" stroke="#fff" stroke-width="2"/><path d="M19 18l8 8" stroke="#fff" stroke-width="4" stroke-linecap="round"/></svg>
    <h2>INSTALLATION</h2>
    <p>Lorem Ipsum is simply dummy text of the printing and typesetting industry. Lorem Ipsum has been the industry's standard dummy text ever since the 1500s, when an unknown printer took...</p>
  </div>
  <div class="service svc-program">
    <svg width="30" height="30" viewBox="0 0 30 30"><rect x="2" y="2" width="26" height="19" rx="1.5" fill="none" stroke="#fff" stroke-width="2"/><path d="M5 12h6l2-4 3 8 2-4h7" fill="none" stroke="#fff" stroke-width="2"/><path d="M15 21v5M9 27h12" stroke="#fff" stroke-width="2"/></svg>
    <h2>PROGRAMMING</h2>
    <p>Lorem Ipsum is simply dummy text of the printing and typesetting industry. Lorem Ipsum has been the industry's standard dummy text ever since the 1500s, when an unknown printer took...</p>
  </div>
</section>

<div class="abs about-photo" role="img" aria-label="Photo of a conference room with wood-panelled wall, wall screen, long table and black chairs"></div>
<section class="abs about-text">
  <div class="kicker">Helping associates to</div>
  <h3>Brightfall Systems</h3>
  <p class="lead">Lorem Ipsum is simply dummy text of the printing and typesetting industry. Lorem Ipsum has been the industry's standard dummy...</p>
  <p class="body">Lorem Ipsum is simply dummy text of the printing and typesetting industry. Lorem Ipsum has been the industry's standard dummy text ever since the 1500s, when an unknown printer took a galley of type and scrambled it to make a type specimen book.</p>
</section>

<h2 class="abs deals-title">BEST DEALS</h2>
<p class="abs deals-intro">Lorem Ipsum is simply dummy text of the printing and typesetting industry. Lorem Ipsum has been the industry's standard dummy text ever since the 1500s, when an unknown printer took a galley of type and scrambled it to make a type specimen book.</p>
<div class="abs deals-rule"></div>
<section class="abs deals">
  <div class="deal" style="width:161px;background:linear-gradient(180deg,#dcdcdc,#9a9a9a)" role="img" aria-label="Photo of a media unit with screen and speakers"><div class="deal-label">Distributed Audio Systems</div></div>
  <div class="deal" style="width:171px;background:linear-gradient(180deg,#f4f4f4,#c9cfc8)" role="img" aria-label="Photo of a ceiling security camera dome"><div class="deal-label">Security Camera Installations</div></div>
  <div class="deal" style="width:171px;background:linear-gradient(180deg,#c9b59a,#6e5c48)" role="img" aria-label="Photo of a lit living room with wall screen"><div class="deal-label">Lighting and Building Automation</div></div>
  <div class="deal" style="width:171px;background:linear-gradient(180deg,#ddd0b8,#8e7b62)" role="img" aria-label="Photo of a home theater room with projector"><div class="deal-label">Home Theaters</div></div>
  <div class="deal" style="width:168px;background:linear-gradient(180deg,#e8e4dc,#b7aa98)" role="img" aria-label="Photo of a meeting with a video call screen"><div class="deal-label">Video Conferencing Systems</div></div>
</section>

<p class="abs cta">FOR MORE DETAILS ABOUT DEAL <a href="#">CLICK HERE</a></p>

<footer class="abs footer">
  <div class="social"><span></span><span></span><span></span></div>
  <p>Copyright 2017. All RIght Reserved.</p>
</footer>
</body>
</html>
```